■レイアウトの希望について
◎全体の左右のサイズは、1000px~1100pxくらいでお願いします。
※左右のサイドにナビを入れる場合は、左右300pxでお願いします。
◎現在のレイアウトは無視してください。
◎重要箇所を目立たせて、全体的にバランスよく配置させてください。
※重要箇所の順位は以下の通りです。
(1)検索ページへの入り口ブロック
(2)記事ページへのナビゲーション
(3)「イチオシ学生会館紹介サイト」と「オススメ学生会館」
(4)「学生会館以外のお部屋探し」
(5)「TOPICS」と「オススメ情報」
※見本のPDFは左ナビがあるようにレイアウトしていますが、トップページは2カラムにせず、1カラムでもかまいません。
(トップページに入れたいブロックを記載しただけですのでレイアウトの希望ではありません)
ただし、サブページは左右どちらかにナビを置く形の2カラムでお願いします。
(サブページのナビに入れるのは、記事ページへのナビゲーションと「学生会館以外のお部屋探し」のみです)

■デザインの希望について
◎落ち着いた感じのバランスの良いデザイン案が希望です。
※色数を多く使ったごちゃごちゃした配置は好みではありません。
※色は派手な感じでなく落ち着いた色が希望ですが、くすんだ色は好みではありません。
◎以前にタスクモアで依頼して作成した下記サイトもご参照ください。
http://www.sorahane-dorm.net/
http://www.qz7.net/
http://www.finerm.com/
http://222.xuu.jp/tomoya.net/
※一番下のみ現在作成中のため仮URLです。(全ページは完成していません)

■その他の希望について
◎ヘッダーはスマホサイズになった場合のことも考えて作成してください。
◎提案内で使用するイメージ画像は無料の素材サイトか、有料画像を使用する場合は、FOLMIOをご利用ください。
https://folmio-img.jp/
※現在サイト内にある画像を使用いただく形でもかまいません。

なお、初回のご提案はできるだけ締切日の2日前までにお願いします。
ギリギリの場合は修正依頼が間に合わず、候補になる良いご提案でも見送る場合がありますので..。

以上になりますので、ご提案のほど、よろしくお願いいたします。
http://www.heyanavi-dorm.net/
3ページ
基本的にはお任せですが、派手な色やくすんだ色は避けてください。(バランスの良い、落ち着いた色が希望)
• 高解像度JPG (.jpg)
• フォトショップ形式 (.psd)
JPG・PNGはどちらでもかまいません。
残り2日になりましたが、提案がないので締切日を延長いたします。

依頼詳細にも記載しましたが、できるだけ締切日の2日前までに初回のご提案をお送りいただけましたら幸いです。

その他、ご要望などがございましたら、メッセージからお送りください。
ロゴは現在のものは使用せず、見本と同様の一般的な横長のものを希望します。
(ロゴではなくて書体をそのまま使用する形でもかまいません)
弊社希望の「全体の左右のサイズは、1000px~1100pxくらい」とうのは、実際に文章や画像が入る本文(左右ナビが入る場合はその外側まで)のサイズになりますので、ご確認ください。

なお、すでにご提案を作成中の場合で、上記に当てはまらない場合はそのまま進めていただいてもかまいません。

とりあえず、デザインが分かれば問題ありませんので..。

※実際にお仕事を依頼することになった場合は、修正をお願いします。
お仕事が決まったあとに作成していただく、サブページのレイアウトを作成しましたので添付します。

決定したトップページと同じ方向性で、こちらのサブページも作成いただく形でお願いします。
今月末まで多忙になり、選考作業や細かい修正依頼作業がすぐにはできそうもないので、締切日をギリギリまで延ばさせていただきます。

必ず当選者は選定させていただきますので、よろしくお願いいたします。

また、依頼金額も若干アップさせていただきました。

全体的なバランスが良く、ごちゃごちゃしていなくて、統一感があり落ち着いた感じのご提案でした。

ご提案をいただき、ありがとうございました。
部分的には気に入ったご提案もあったのですが、全体的なバランスやメリハリといった点で、採用した案を選びました。
申し訳ございませんがご了承ください。
なお、今後も複数サイトのリニューアル依頼をタスクモアに出しますので、機会がございましたら、よろしくお願いいたします。

```html
<!DOCTYPE html>
<html lang="ja">
<head>
<meta charset="UTF-8">
<title>すみか学生会館ナビ</title>
<link rel="stylesheet" href="https://fonts.googleapis.com/css2?family=Noto+Sans+JP:wght@400;500;700&display=swap">
<style>
:root{
  --green:#8cbf26;
  --green-dark:#6f9c14;
  --green-pale:#eef6dc;
  --cream:#fbf5dc;
  --text:#444;
  --muted:#888;
  --line:#dcdcdc;
  --white:#fff;
  --footer:#9cc93a;
}
*{box-sizing:border-box;margin:0;padding:0}
html,body{width:1200px;height:3004px;overflow:hidden}
body{font-family:"Noto Sans JP",sans-serif;color:var(--text);background:var(--white);font-size:14px;line-height:1.6}
.inner{width:1000px;margin:0 auto;position:relative}

/* header */
.site-header{height:60px;background:var(--white)}
.site-header .inner{display:flex;align-items:center;height:60px;justify-content:space-between}
.brand{display:flex;align-items:center;gap:10px;font-weight:700;font-size:26px;color:var(--green-dark)}
.brand-mark{width:22px;height:22px;background:var(--green);border-radius:50%}
.header-lead{width:520px;font-size:12px;color:var(--muted);line-height:1.5}

/* hero */
.hero{height:340px;display:flex}
.hero-photo{flex:1}
.hero-photo:nth-child(1){background:linear-gradient(160deg,#d9cbb8,#b8a48c)}
.hero-photo:nth-child(2){background:linear-gradient(160deg,#c6d3dc,#93a7b5)}
.hero-photo:nth-child(3){background:linear-gradient(160deg,#efe2d2,#c7b09a)}
.hero-photo:nth-child(4){background:linear-gradient(160deg,#cfd6de,#7f8d99)}
.hero-photo:nth-child(5){background:linear-gradient(160deg,#e4d7c6,#a89580)}

/* search */
.search-panel{width:760px;margin:-20px auto 0;position:relative;background:var(--white);box-shadow:0 3px 12px rgba(0,0,0,.15);padding:0 40px 36px}
.search-title{background:var(--green);color:var(--white);text-align:center;font-size:22px;font-weight:700;letter-spacing:.08em;height:58px;line-height:58px;margin:0 -40px 26px;position:relative}
.search-title::after{content:"";position:absolute;left:50%;bottom:-10px;margin-left:-10px;border:10px solid transparent;border-bottom:0;border-top-color:var(--green)}
.school-search{display:flex;align-items:center;gap:16px}
.school-search label{font-weight:700;font-size:15px;white-space:nowrap}
.school-input{flex:1;height:44px;border:1px solid var(--line);border-radius:3px;display:flex;align-items:center;padding:0 14px;gap:10px;color:#aaa;font-size:13px;background:#fafafa}
.search-note{font-size:12px;color:var(--muted);margin:14px 0 22px;line-height:1.7}
.search-buttons{display:flex;gap:22px;justify-content:center}
.search-btn{width:200px;height:82px;background:var(--green);border-radius:4px;color:var(--white);display:flex;align-items:center;justify-content:center;gap:10px;font-size:17px;font-weight:700;box-shadow:0 3px 0 var(--green-dark)}
.search-btn small{font-size:12px;font-weight:500}

/* section heading */
.section-heading{text-align:center;font-size:26px;font-weight:700;color:var(--green-dark);letter-spacing:.1em}
.section-heading::after{content:"";display:block;width:60px;height:3px;background:var(--green);margin:10px auto 0}

/* about grid */
.about{padding-top:60px}
.about-grid{display:grid;grid-template-columns:repeat(4,235px);gap:34px 20px;margin-top:40px}
.about-card .thumb{height:170px}
.about-card p{margin-top:10px;font-size:14px;font-weight:500;display:flex;align-items:center;gap:8px}
.about-card p::before{content:"";width:8px;height:8px;background:var(--green);border-radius:50%;flex:none}
.t1{background:linear-gradient(150deg,#e8ddd0,#bba792)}
.t2{background:linear-gradient(150deg,#f0e6de,#c9b7a6)}
.t3{background:linear-gradient(150deg,#dfe4e8,#a4afb8)}
.t4{background:linear-gradient(150deg,#e9dccd,#c1a27e)}
.t5{background:linear-gradient(150deg,#d8c9b6,#8d7b66)}
.t6{background:linear-gradient(150deg,#e4e7ea,#aeb6bd)}
.t7{background:linear-gradient(150deg,#ece1d6,#bda995)}
.t8{background:linear-gradient(150deg,#e9cfa2,#b9803c)}

/* recommend band */
.recommend{background:var(--cream);margin-top:70px;height:500px;padding-top:46px}
.recommend-grid{display:flex;justify-content:center;gap:30px;margin-top:40px}
.rec-card{width:240px;background:var(--white);box-shadow:0 2px 6px rgba(0,0,0,.1);padding:12px 12px 18px}
.rec-card .thumb{height:160px}
.rec-card h3{font-size:14px;color:var(--green-dark);margin-top:12px;display:flex;align-items:center;gap:6px}
.rec-card h3::before{content:"";width:8px;height:8px;background:var(--green);border-radius:50%}
.rec-card p{font-size:12px;color:var(--muted);line-height:1.6;margin-top:4px}
.r1{background:linear-gradient(150deg,#d9e6c8,#9cb57a)}
.r2{background:linear-gradient(150deg,#c98f6c,#8f5a3c)}
.r3{background:linear-gradient(150deg,#e5d0a4,#b58a44)}

/* lower */
.lower{padding-top:60px}
.lower .inner{display:flex;justify-content:space-between}
.side{width:260px}
.main{width:700px}
.block-title{font-size:17px;font-weight:700;border-left:4px solid var(--green);padding-left:10px;line-height:1.3;margin-bottom:16px}
.link-list{list-style:none;border-top:1px solid var(--line)}
.link-list li{font-size:12px;line-height:1.6;padding:10px 0 10px 16px;border-bottom:1px dotted var(--line);position:relative}
.link-list li::before{content:"";position:absolute;left:2px;top:16px;border:4px solid transparent;border-right:0;border-left:5px solid var(--green)}
.side .block+.block{margin-top:40px}
.banner-grid{display:grid;grid-template-columns:repeat(2,340px);gap:16px 20px}
.banner{height:92px;border:1px solid var(--line);display:flex;align-items:center;justify-content:space-between;padding-left:20px;overflow:hidden;background:var(--white)}
.banner span{font-size:17px;font-weight:700;color:var(--green-dark)}
.banner .thumb{width:120px;height:100%}
.b1{background:linear-gradient(150deg,#eadfd3,#c4ad97)}
.b2{background:linear-gradient(150deg,#f2e6e9,#cfa9b4)}
.b3{background:linear-gradient(150deg,#efe3d5,#c9b29a)}
.b4{background:linear-gradient(150deg,#f0e3e6,#c7a2ab)}
.main .block+.block{margin-top:44px}
.room-grid{display:grid;grid-template-columns:repeat(3,220px);gap:16px 20px}
.room-link{height:64px;background:var(--green-pale);display:flex;align-items:center;gap:12px;padding-right:10px;font-size:13px;font-weight:500}
.room-link .thumb{width:78px;height:64px;flex:none}
.m1{background:linear-gradient(150deg,#e6dccd,#b9a58e)}
.m2{background:linear-gradient(150deg,#dbe3ea,#9fb0bf)}
.m3{background:linear-gradient(150deg,#eee3d6,#c2ab93)}
.m4{background:linear-gradient(150deg,#e3e9dc,#a7b895)}
.m5{background:linear-gradient(150deg,#efe1d4,#c8a88a)}
.m6{background:linear-gradient(150deg,#dde4e7,#a2b2b9)}

/* footer */
.site-footer{position:absolute;left:0;top:2940px;width:1200px;height:64px;background:var(--footer);color:var(--white)}
.site-footer .inner{display:flex;justify-content:space-between;align-items:center;height:64px;font-size:12px}
.footer-nav{display:flex;gap:28px}
</style>
</head>
<body>

<header class="site-header">
  <div class="inner">
    <div class="brand"><span class="brand-mark"></span>すみか学生会館ナビ</div>
    <p class="header-lead">学生のための安心・快適な住まい「学生会館」の魅力と情報を、わかりやすくご紹介。あなたにぴったりのお部屋探しをお手伝いします。</p>
  </div>
</header>

<section class="hero">
  <div class="hero-photo" role="img" aria-label="学生の写真"></div>
  <div class="hero-photo" role="img" aria-label="学生の写真"></div>
  <div class="hero-photo" role="img" aria-label="学生の写真"></div>
  <div class="hero-photo" role="img" aria-label="学生の写真"></div>
  <div class="hero-photo" role="img" aria-label="学生の写真"></div>
</section>

<section class="search-panel">
  <h2 class="search-title">学生会館で安心・快適な住まいを</h2>
  <div class="school-search">
    <label>学校名で探す</label>
    <div class="school-input">
      <svg width="16" height="16" viewBox="0 0 16 16"><circle cx="7" cy="7" r="5" fill="none" stroke="#aaa" stroke-width="2"/><line x1="11" y1="11" x2="15" y2="15" stroke="#aaa" stroke-width="2"/></svg>
      学校名を入力してください（例：〇〇大学）
    </div>
  </div>
  <p class="search-note">全国の大学・短大・専門学校の近くにある学生会館をまとめてご紹介しています。<br>食事付きや女子専用など、条件に合わせてお部屋を探すことができます。</p>
  <div class="search-buttons">
    <div class="search-btn">
      <svg width="26" height="26" viewBox="0 0 26 26"><rect x="5" y="2" width="16" height="17" rx="4" fill="none" stroke="#fff" stroke-width="2.4"/><line x1="5" y1="11" x2="21" y2="11" stroke="#fff" stroke-width="2"/><line x1="8" y1="20" x2="5" y2="25" stroke="#fff" stroke-width="2.4"/><line x1="18" y1="20" x2="21" y2="25" stroke="#fff" stroke-width="2.4"/></svg>
      <span>路線<small>から探す</small></span>
    </div>
    <div class="search-btn">
      <svg width="22" height="28" viewBox="0 0 22 28"><path d="M11 1a9 9 0 0 1 9 9c0 7-9 17-9 17S2 17 2 10a9 9 0 0 1 9-9z" fill="#fff"/><circle cx="11" cy="10" r="3.5" fill="#8cbf26"/></svg>
      <span>地域<small>から探す</small></span>
    </div>
    <div class="search-btn">
      <svg width="26" height="26" viewBox="0 0 26 26"><circle cx="13" cy="14" r="9" fill="none" stroke="#fff" stroke-width="2.4"/><line x1="2" y1="3" x2="2" y2="24" stroke="#fff" stroke-width="2"/><line x1="24" y1="3" x2="24" y2="24" stroke="#fff" stroke-width="2"/></svg>
      <span>食事付き<small>を探す</small></span>
    </div>
  </div>
</section>

<section class="about">
  <div class="inner">
    <h2 class="section-heading">学生会館を知る</h2>
    <div class="about-grid">
      <div class="about-card"><div class="thumb t1" role="img" aria-label="学生会館で過ごす学生の写真"></div><p>学生会館ってどんなところ？</p></div>
      <div class="about-card"><div class="thumb t2" role="img" aria-label="入館手続きの写真"></div><p>学生会館入館の流れ</p></div>
      <div class="about-card"><div class="thumb t3" role="img" aria-label="建物外観の写真"></div><p>学生会館 VS アパート・寮</p></div>
      <div class="about-card"><div class="thumb t4" role="img" aria-label="館内の様子の写真"></div><p>特集・学生会館レポート</p></div>
      <div class="about-card"><div class="thumb t5" role="img" aria-label="質問と回答を表す写真"></div><p>学生会館 Q&amp;A</p></div>
      <div class="about-card"><div class="thumb t6" role="img" aria-label="設備の写真"></div><p>設備の紹介</p></div>
      <div class="about-card"><div class="thumb t7" role="img" aria-label="学生会館の一日の写真"></div><p>学生会館の一日</p></div>
      <div class="about-card"><div class="thumb t8" role="img" aria-label="食事メニューの写真"></div><p>学生会館の食事</p></div>
    </div>
  </div>
</section>

<section class="recommend">
  <h2 class="section-heading">オススメ学生会館</h2>
  <div class="recommend-grid">
    <div class="rec-card"><div class="thumb r1" role="img" aria-label="学生会館の写真"></div><h3>緑風学生会館</h3><p>駅から徒歩5分、緑に囲まれた落ち着いた環境の学生会館です。</p></div>
    <div class="rec-card"><div class="thumb r2" role="img" aria-label="学生会館の外観写真"></div><h3>桜川ドミトリー</h3><p>朝・夕食付きで安心。複数の大学へ通いやすい立地です。</p></div>
    <div class="rec-card"><div class="thumb r3" role="img" aria-label="食事の写真"></div><h3>陽光学生会館</h3><p>栄養バランスの良い手作りの食事が自慢の学生会館です。</p></div>
  </div>
</section>

<section class="lower">
  <div class="inner">
    <aside class="side">
      <div class="block">
        <h2 class="block-title">TOPICS</h2>
        <ul class="link-list">
          <li>学生会館の新生活応援キャンペーンを実施中です</li>
          <li>一人暮らしに役立つ生活情報の特集を公開しました</li>
          <li>学生マンションとの違いを比較ページで解説</li>
          <li>春からの新入生向け入館案内を更新しました</li>
          <li>保護者の方向けの安心ガイドを掲載</li>
        </ul>
      </div>
      <div class="block">
        <h2 class="block-title">オススメ情報</h2>
        <ul class="link-list">
          <li>学生マンション・学生寮の選び方</li>
          <li>学生会館の費用について</li>
          <li>女子学生に人気の学生会館</li>
          <li>食事付き学生会館の魅力</li>
          <li>新生活の準備チェックリスト</li>
          <li>大学周辺の住まい情報</li>
        </ul>
      </div>
    </aside>
    <div class="main">
      <div class="block">
        <h2 class="block-title">イチオシ学生会館紹介サイト</h2>
        <div class="banner-grid">
          <div class="banner"><span>ひだまり学生会館</span><div class="thumb b1" role="img" aria-label="学生の写真"></div></div>
          <div class="banner"><span>女子学生寮ガイド</span><div class="thumb b2" role="img" aria-label="女子学生の写真"></div></div>
          <div class="banner"><span>学生寮インフォ</span><div class="thumb b3" role="img" aria-label="学生の写真"></div></div>
          <div class="banner"><span>ミモザ女子学生会館</span><div class="thumb b4" role="img" aria-label="女子学生の写真"></div></div>
        </div>
      </div>
      <div class="block">
        <h2 class="block-title">学生会館以外のお部屋探し</h2>
        <div class="room-grid">
          <div class="room-link"><div class="thumb m1" role="img" aria-label="マンションの写真"></div>マンション・アパート探し</div>
          <div class="room-link"><div class="thumb m2" role="img" aria-label="建物の写真"></div>学生マンションを探す</div>
          <div class="room-link"><div class="thumb m3" role="img" aria-label="部屋の写真"></div>下宿の部屋探し</div>
          <div class="room-link"><div class="thumb m4" role="img" aria-label="寮の写真"></div>女子学生寮を探す</div>
          <div class="room-link"><div class="thumb m5" role="img" aria-label="室内の写真"></div>学生寮の部屋を探す</div>
          <div class="room-link"><div class="thumb m6" role="img" aria-label="ワンルームの写真"></div>ワンルームを探す</div>
        </div>
      </div>
    </div>
  </div>
</section>

<footer class="site-footer">
  <div class="inner">
    <nav class="footer-nav"><span>運営会社</span><span>プライバシーポリシー</span><span>サイトマップ</span><span>お問い合わせ</span></nav>
    <small>Copyright (C) すみか学生会館ナビ All Rights Reserved.</small>
  </div>
</footer>

</body>
</html>
```